Need Epic Web Banner for New Site

We need a banner for our web page. We are BrightMorrow.com, think of us as the Fendlow of the highest quality sports nutrition supplements on the web. Our site is under construction, if you visit our site, this banner will go at the very top above the menu bar. We are marketing supplements a different way then most; we are staying away from hulked out guys on steroids & gimmick magic pills/ slogans. We are all about clean quality products with less ingredients.

We are attaching our logo/ symbol & a text we made in AI for a point of reference. Please help us bring our site and vision of BrightMorrow to life!

We are not married to the colors but GREEN is a must!
Updates

Disregard previous message about Rosa's entry. This platform does not allow me to delet comments I post.

Target Market(s)

Heath Consious, Health Seekers, Active Fit People, Gym Rats, Rock Climbers

Industry/Entity Type

Nutrition

Font styles to use
Other font styles liked:
• Semplicita

Colors
33b8a4
00a990
86cfc6

Requirements
Must have
• For text In addition to BrightMorrow.com we'd like "Not all supplements are created equal"

```html
<!DOCTYPE html>
<html lang="en">
<head>
<meta charset="utf-8">
<title>BrightMorrow.com – Web Banner</title>
<link rel="stylesheet" href="https://fonts.googleapis.com/css2?family=Open+Sans:wght@400;600&display=swap">
<style>
  :root {
    --page-bg: #e7e8e9;
    --banner-black: #050505;
    --brand-green: #76c043;
    --brand-green-dark: #5fa834;
    --swoosh-grey: #cfd0d1;
    --headline-white: #ffffff;
    --photo-shadow: #141414;
    --photo-skin-dark: #4e4e4e;
    --photo-skin-light: #9a9a9a;
  }
  * { box-sizing: border-box; margin: 0; padding: 0; }
  html, body {
    width: 1200px;
    height: 669px;
    overflow: hidden;
    background: var(--page-bg);
    font-family: "Open Sans", Arial, sans-serif;
  }
  .banner {
    position: absolute;
    left: 145px;
    top: 153px;
    width: 919px;
    height: 343px;
    background: var(--banner-black);
    overflow: hidden;
  }
  .banner__photo {
    position: absolute;
    left: 330px;
    top: 0;
    width: 589px;
    height: 343px;
    background:
      linear-gradient(to bottom, transparent 62%, var(--banner-black) 88%),
      linear-gradient(90deg, var(--banner-black) 0%, transparent 22%),
      radial-gradient(ellipse 150px 260px at 520px 130px, var(--photo-skin-light) 0%, var(--photo-skin-dark) 50%, transparent 85%),
      radial-gradient(ellipse 210px 240px at 240px 150px, #858585 0%, var(--photo-skin-dark) 50%, transparent 82%),
      linear-gradient(90deg, var(--banner-black) 0%, var(--photo-shadow) 45%, #1e1e1e 100%);
  }
  .banner__waves {
    position: absolute;
    left: 0;
    top: 0;
    width: 919px;
    height: 343px;
  }
  .headline {
    position: absolute;
    left: 36px;
    top: 17px;
    font-size: 36px;
    font-weight: 400;
    line-height: 46px;
    color: var(--headline-white);
  }
  .headline__accent { color: var(--brand-green); }
  .brand-name {
    position: absolute;
    left: 36px;
    top: 262px;
    display: flex;
    align-items: center;
    gap: 8px;
    font-size: 22px;
    font-weight: 600;
    color: var(--brand-green);
  }
  .brand-name__mark {
    width: 14px;
    height: 14px;
    background: var(--brand-green);
  }
</style>
</head>
<body>
  <section class="banner">
    <div class="banner__photo" role="img" aria-label="Black and white photo of a muscular man seen from the back and a focused woman in a fighting stance"></div>

    <svg class="banner__waves" viewBox="0 0 1149 429" preserveAspectRatio="none" aria-hidden="true">
      <path fill="var(--brand-green)" d="M0,400 C250,435 500,395 700,352 C850,320 950,305 1030,328 C1090,348 1130,382 1149,398 L1149,429 L0,429 Z"/>
      <path fill="var(--banner-black)" d="M450,429 C600,392 740,362 860,352 C960,344 1040,362 1100,405 L1149,429 Z"/>
      <path fill="var(--swoosh-grey)" d="M750,380 C830,355 910,346 970,348 C1030,352 1080,385 1110,429 L1000,429 C980,400 930,378 850,372 Z"/>
      <path fill="var(--brand-green-dark)" d="M1110,429 C1080,390 1050,365 1030,352 C1080,365 1125,390 1149,405 L1149,429 Z"/>
    </svg>

    <h1 class="headline">
      NOT ALL<br>
      <span class="headline__accent">SUPPLEMENTS</span><br>
      ARE CREATED EQUAL
    </h1>

    <div class="brand-name">
      <span class="brand-name__mark"></span>
      <span>BrightMorrow.com</span>
    </div>
  </section>
</body>
</html>
```